Calder Pizza - Takeout Menu Design

We are looking for a takeout menu design.
We are looking for a( 5" x 8.5" DOUBLE SIDED) flyer with our available pizza flavors
Must be easy to ready and not "busy"

Must include our logo (attached)
website: www.calderpizza.ca
address:
Fenwick Ridge Plaza
417, 318 9 Avenue SW
and the following details:
Visit our website for our complete appetizer, pasta, salad and catering menu.

Winner of this contest will also be offered to create a few print designs via printhive.

Please do not hesitate to ask any questions.

Target Market(s)

Business / Office clientele

Industry/Entity Type

Pizza place / specializing in corporate orders

Requirements
Must have
• Easy to read
Should not have
• Can not be busy or cluttered

```html
<!DOCTYPE html>
<html lang="en">
<head>
<meta charset="utf-8">
<title>Calder Pizza – Takeout Menu</title>
<link href="https://fonts.googleapis.com/css2?family=Montserrat:wght@400;600;700;800;900&family=Poppins:wght@400;500;600;700&family=Great+Vibes&display=swap" rel="stylesheet">
<style>
:root{
  --stage:#dedede;
  --red:#c8251d;
  --red-deep:#b51f18;
  --ink:#1c1c1c;
  --tag-dark:#2e2e2e;
  --black:#0a0a0a;
  --wood-1:#f7f7f6;
  --wood-2:#e9e9e7;
  --white:#ffffff;
  --muted:#3a3a3a;
}
*{box-sizing:border-box;margin:0;padding:0}
html,body{width:1200px;height:1200px;overflow:hidden}
body{background:var(--stage);position:relative;font-family:"Poppins",sans-serif;color:var(--ink)}
.page{position:absolute;top:131px;width:547px;height:930px;overflow:hidden;background:var(--black)}
.page--front{left:46px}
.page--back{left:621px}
.abs{position:absolute}
.wood{background:linear-gradient(100deg,var(--wood-1) 0%,var(--wood-2) 30%,var(--wood-1) 55%,var(--wood-2) 80%,var(--wood-1) 100%)}
.photo{position:absolute;border-radius:50%}
.photo--pizza{background:radial-gradient(circle at 50% 45%,#f3e2b8 0%,#e8b060 45%,#d2873a 70%,#b86a2a 100%)}
.photo--pizza-red{background:radial-gradient(circle at 50% 45%,#f1c48a 0%,#e08a3c 40%,#c8462a 75%,#a8571f 100%)}
.photo--bowl{background:radial-gradient(circle,#f1eee9 0%,#ddd6cc 55%,#b86b32 72%,#8f4c20 100%)}
.photo--sauce{background:radial-gradient(circle,#c01b14 0%,#a51410 60%,#e8e4df 78%,#d6d1cb 100%)}
.photo--tomato{background:radial-gradient(circle at 40% 40%,#f0473a 0%,#c8231a 100%)}
.photo--leaf{border-radius:50% 0 50% 0;background:linear-gradient(135deg,#5aa03a,#2f7a22)}

/* front */
.front-logo{left:0;width:547px;top:38px;text-align:center;font-family:"Montserrat",sans-serif;font-weight:400;font-size:34px;letter-spacing:1px;color:var(--white)}
.front-script{left:185px;top:82px;font-family:"Great Vibes",cursive;font-size:64px;color:var(--white);transform:rotate(-6deg);z-index:2}
.front-title{left:0;width:547px;top:118px;text-align:center;font-family:"Montserrat",sans-serif;font-weight:900;font-size:104px;line-height:1;letter-spacing:-3px;color:var(--white)}
.section-title{font-family:"Montserrat",sans-serif;font-weight:800;color:var(--ink);white-space:nowrap}
.section-title em{font-style:normal;color:var(--red)}
.classic-title{left:102px;top:438px;font-size:19px}
.col-head{font-family:"Montserrat",sans-serif;font-weight:800;color:var(--red);text-align:center}
.classic-name{left:70px;font-weight:600;font-size:15px;line-height:18px;color:var(--ink)}
.tag{position:absolute;display:flex;align-items:center;justify-content:center;color:var(--white);font-weight:700;
  clip-path:polygon(0 0,100% 0,calc(100% - 7px) 50%,100% 100%,0 100%,7px 50%)}
.tag--dark{background:var(--tag-dark)}
.tag--red{background:var(--red)}
.tag--lg{height:25px;width:80px;font-size:13px}
.tag--lg.tag--dark{left:290px}
.tag--lg.tag--red{left:398px}
.front-note{left:68px;top:774px;font-size:12.5px;line-height:15px;color:var(--ink);width:270px}
.small-note{font-size:9.5px;line-height:11px;color:var(--ink)}
.web{font-family:"Montserrat",sans-serif;font-weight:500;font-size:17.5px;color:var(--ink)}
.web strong{color:var(--red);font-weight:700}

/* back */
.special-title{left:0;width:547px;text-align:center;top:50px;font-size:20px}
.item{position:absolute;width:112px}
.item--l{left:47px}
.item--r{left:288px;width:104px}
.item h3{font-family:"Poppins",sans-serif;font-weight:600;font-size:10px;line-height:11px;color:var(--ink)}
.item p{font-size:8.2px;line-height:9.7px;color:var(--muted);margin-top:1px}
.tag--sm{height:18px;width:49px;font-size:10px}
.pl .tag--dark{left:157px}
.pl .tag--red{left:211px}
.pr .tag--dark{left:397px}
.pr .tag--red{left:452px}
.pill{left:288px;top:604px;width:95px;height:13px;border-radius:7px;background:#d6d6d6;font-family:"Montserrat",sans-serif;font-weight:700;font-size:8.5px;line-height:13px;text-align:center;color:var(--ink)}
.back-logo{left:49px;top:688px;font-family:"Montserrat",sans-serif;font-weight:400;font-size:27px;letter-spacing:1px;color:var(--ink)}
.address{left:74px;top:727px;font-size:12.5px;line-height:14.5px;color:var(--ink)}
.pork{left:289px;top:679px;width:213px;height:51px;border-radius:12px;background:var(--red);color:var(--white)}
.pork h4{position:absolute;left:12px;top:12px;font-family:"Poppins",sans-serif;font-weight:700;font-size:11px}
.pork p{position:absolute;left:12px;top:30px;font-size:7.8px}
.pork .mini{position:absolute;top:13px;height:11px;width:35px;font-size:7px;display:flex;align-items:center;justify-content:center;font-weight:700;
  clip-path:polygon(0 0,100% 0,calc(100% - 4px) 50%,100% 100%,0 100%,4px 50%)}
.mini--dark{left:133px;background:var(--tag-dark);color:var(--white)}
.mini--light{left:170px;background:var(--white);color:var(--ink)}
</style>
</head>
<body>

<!-- FRONT -->
<section class="page page--front">
  <svg class="abs" width="547" height="930" viewBox="0 0 547 930" aria-hidden="true" style="left:0;top:0">
    <defs>
      <linearGradient id="woodF" x1="0" x2="1" y1="0" y2="0.1">
        <stop offset="0" stop-color="#f7f7f6"/><stop offset=".3" stop-color="#e9e9e7"/><stop offset=".6" stop-color="#f8f8f7"/><stop offset="1" stop-color="#ebebe9"/>
      </linearGradient>
    </defs>
    <rect width="547" height="930" fill="#0a0a0a"/>
    <path d="M21 140 H526 V888 a20 20 0 0 1 -20 20 H41 a20 20 0 0 1 -20 -20 Z" fill="url(#woodF)"/>
    <polygon points="0,0 547,0 547,147 273,259 0,147" fill="#c8251d"/>
  </svg>

  <div class="abs front-logo">CALDER PIZZA</div>
  <div class="abs front-script">Takeout</div>
  <div class="abs front-title">MENU</div>

  <div class="photo photo--pizza" role="img" aria-label="Photo of a margherita pizza with cherry tomatoes, mozzarella and basil" style="left:114px;top:206px;width:322px;height:216px;border-radius:0 0 50% 50%"></div>
  <div class="photo photo--bowl" role="img" aria-label="Photo of a wooden bowl of fresh mozzarella balls" style="left:36px;top:259px;width:112px;height:112px"></div>
  <div class="photo photo--sauce" role="img" aria-label="Photo of a cup of tomato sauce" style="left:404px;top:322px;width:78px;height:78px"></div>
  <div class="photo photo--tomato" role="img" aria-label="Photo of a cherry tomato" style="left:426px;top:209px;width:40px;height:46px"></div>

  <h2 class="abs section-title classic-title">CLASSIC TAKE-OUT PIZZA - <em>8” &amp; 13”</em></h2>
  <div class="abs col-head" style="left:310px;top:466px;width:50px;font-size:17px">8”</div>
  <div class="abs col-head" style="left:418px;top:466px;width:50px;font-size:17px">13”</div>

  <div class="abs classic-name" style="top:484px">Pepperoni &amp;<br>Mushroom</div>
  <div class="tag tag--lg tag--dark" style="top:490px">$12.99</div><div class="tag tag--lg tag--red" style="top:490px">$30.95</div>

  <div class="abs classic-name" style="top:530px">Pepperoni</div>
  <div class="tag tag--lg tag--dark" style="top:528px">$11.99</div><div class="tag tag--lg tag--red" style="top:528px">$29.95</div>

  <div class="abs classic-name" style="top:565px">Hawaiian</div>
  <div class="tag tag--lg tag--dark" style="top:562px">$12.99</div><div class="tag tag--lg tag--red" style="top:562px">$30.95</div>

  <div class="abs classic-name" style="top:599px">Beef &amp; Mushroom</div>
  <div class="tag tag--lg tag--dark" style="top:597px">$13.49</div><div class="tag tag--lg tag--red" style="top:597px">$32.95</div>

  <div class="abs classic-name" style="top:634px">Pepperoni &amp; Ham</div>
  <div class="tag tag--lg tag--dark" style="top:631px">$12.99</div><div class="tag tag--lg tag--red" style="top:631px">$30.95</div>

  <div class="abs classic-name" style="top:668px">Ham &amp; Mushroom</div>
  <div class="tag tag--lg tag--dark" style="top:666px">$12.99</div><div class="tag tag--lg tag--red" style="top:666px">$30.95</div>

  <div class="abs classic-name" style="top:703px">Beef &amp; Onion</div>
  <div class="tag tag--lg tag--dark" style="top:700px">$13.49</div><div class="tag tag--lg tag--red" style="top:700px">$32.95</div>

  <div class="abs classic-name" style="top:737px">Cheese</div>
  <div class="tag tag--lg tag--dark" style="top:735px">$11.99</div><div class="tag tag--lg tag--red" style="top:735px">$29.95</div>

  <p class="abs front-note">All of our pizzas are prepared fresh everyday using only the finest mozzarella blend and ingredients.</p>
  <p class="abs small-note" style="left:68px;top:830px;width:220px">For our complete appetizer, pasta, salad and catering menu visit our website</p>
  <p class="abs web" style="left:68px;top:861px">www.<strong>calderpizza</strong>.ca</p>

  <div class="photo photo--pizza-red" role="img" aria-label="Photo of a sliced vegetable pizza on a wooden board" style="left:324px;top:786px;width:190px;height:190px"></div>
  <div class="photo photo--tomato" role="img" aria-label="Photo of a cherry tomato" style="left:298px;top:856px;width:28px;height:30px"></div>
  <div class="photo photo--leaf" role="img" aria-label="Photo of a basil leaf" style="left:478px;top:780px;width:36px;height:26px"></div>
</section>

<!-- BACK -->
<section class="page page--back">
  <svg class="abs" width="547" height="930" viewBox="0 0 547 930" aria-hidden="true" style="left:0;top:0">
    <defs>
      <linearGradient id="woodB" x1="0" x2="1" y1="0" y2="0.1">
        <stop offset="0" stop-color="#f7f7f6"/><stop offset=".3" stop-color="#e9e9e7"/><stop offset=".6" stop-color="#f8f8f7"/><stop offset="1" stop-color="#ebebe9"/>
      </linearGradient>
    </defs>
    <rect width="547" height="930" fill="#0a0a0a"/>
    <rect width="547" height="462" fill="#c8251d"/>
    <rect x="21" y="23" width="505" height="885" rx="18" fill="url(#woodB)"/>
  </svg>

  <h2 class="abs section-title special-title">SPECIALTY TAKE-OUT PIZZA- <em>8” &amp; 13”</em></h2>
  <div class="abs col-head" style="left:170px;top:84px;width:30px;font-size:13px">8”</div>
  <div class="abs col-head" style="left:221px;top:84px;width:30px;font-size:13px">13”</div>
  <div class="abs col-head" style="left:414px;top:84px;width:30px;font-size:13px">8”</div>
  <div class="abs col-head" style="left:465px;top:84px;width:30px;font-size:13px">13”</div>

  <!-- left column -->
  <div class="item item--l" style="top:102px"><h3>All Meat</h3><p>Pepperoni, Beef &amp;<br>Smoked Ham &amp; Bacon</p></div>
  <div class="pl"><div class="tag tag--sm tag--dark" style="top:104px">$11.99</div><div class="tag tag--sm tag--red" style="top:104px">$29.95</div></div>

  <div class="item item--l" style="top:144px"><h3>Double Pepperoni</h3><p>Loads of Pepperoni</p></div>
  <div class="pl"><div class="tag tag--sm tag--dark" style="top:143px">$11.99</div><div class="tag tag--sm tag--red" style="top:143px">$29.95</div></div>

  <div class="item item--l" style="top:174px;width:115px"><h3>Hot Honey Pepperoni</h3><p>Double Pepperoni and<br>drizzled with Hot Honey</p></div>
  <div class="pl"><div class="tag tag--sm tag--dark" style="top:176px">$11.99</div><div class="tag tag--sm tag--red" style="top:176px">$29.95</div></div>

  <div class="item item--l" style="top:215px"><h3>Hawaiian Heat</h3><p>Smoked Ham, Pineapple<br>and Banana Peppers</p></div>
  <div class="pl"><div class="tag tag--sm tag--dark" style="top:217px">$11.99</div><div class="tag tag--sm tag--red" style="top:217px">$29.95</div></div>

  <div class="item item--l" style="top:255px"><h3>Four Cheese</h3><p>Mozzarella, Feta,<br>Romano and Cheddar<br>Cheese</p></div>
  <div class="pl"><div class="tag tag--sm tag--dark" style="top:258px">$11.99</div><div class="tag tag--sm tag--red" style="top:258px">$29.95</div></div>

  <div class="item item--l" style="top:306px"><h3>Montreal</h3><p>Pepperoni &amp; Double<br>Smoked Bacon</p></div>
  <div class="pl"><div class="tag tag--sm tag--dark" style="top:307px">$11.99</div><div class="tag tag--sm tag--red" style="top:307px">$29.95</div></div>

  <div class="item item--l" style="top:347px"><h3>Montreal Heat</h3><p>Pepperoni, Double<br>Smoked Bacon &amp;<br>Banana Peppers</p></div>
  <div class="pl"><div class="tag tag--sm tag--dark" style="top:347px">$11.99</div><div class="tag tag--sm tag--red" style="top:347px">$29.95</div></div>

  <div class="item item--l" style="top:395px"><h3>Supreme</h3><p>Pepperoni, Mushrooms<br>&amp; Green Peppers</p></div>
  <div class="pl"><div class="tag tag--sm tag--dark" style="top:396px">$11.99</div><div class="tag tag--sm tag--red" style="top:396px">$29.95</div></div>

  <div class="item item--l" style="top:434px"><h3>Canadian</h3><p>Pepperoni, Mushrooms<br>&amp; Ham</p></div>
  <div class="pl"><div class="tag tag--sm tag--dark" style="top:435px">$11.99</div><div class="tag tag--sm tag--red" style="top:435px">$29.95</div></div>

  <div class="item item--l" style="top:477px"><h3>BBQ Chicken</h3><p>Chicken Breast, Hickory<br>BBQ Sauce &amp; Red Onions</p></div>
  <div class="pl"><div class="tag tag--sm tag--dark" style="top:478px">$11.99</div><div class="tag tag--sm tag--red" style="top:478px">$29.95</div></div>

  <div class="item item--l" style="top:517px"><h3>BBQ Chicken Plus</h3><p>Chicken Breast, Hickory<br>BBQ Sauce, Red Onions<br>&amp; Cilantro</p></div>
  <div class="pl"><div class="tag tag--sm tag--dark" style="top:518px">$11.99</div><div class="tag tag--sm tag--red" style="top:518px">$29.95</div></div>

  <div class="item item--l" style="top:567px"><h3>Sweet Chili Chicken</h3><p>Chicken Breast,<br>Pineapple, Red Onions &amp;<br>Sweet Chili Sauce</p></div>
  <div class="pl"><div class="tag tag--sm tag--dark" style="top:568px">$11.99</div><div class="tag tag--sm tag--red" style="top:568px">$29.95</div></div>

  <div class="item item--l" style="top:620px"><h3>Chicken Club</h3><p>Chicken Breast, Double<br>Smoked Bacon, Red<br>Onions and Tomatoes</p></div>
  <div class="pl"><div class="tag tag--sm tag--dark" style="top:618px">$11.99</div><div class="tag tag--sm tag--red" style="top:618px">$29.95</div></div>

  <!-- right column -->
  <div class="item item--r" style="top:102px"><h3>Athenean</h3><p>Chicken Breast, Spinach,<br>Feta Cheese and<br>Tomato</p></div>
  <div class="pr"><div class="tag tag--sm tag--dark" style="top:104px">$11.99</div><div class="tag tag--sm tag--red" style="top:104px">$29.95</div></div>

  <div class="item item--r" style="top:149px"><h3>Greek Supreme</h3><p>Chicken Breast, Feta<br>Cheese, Tomato, Green<br>Pepper, Red Onions &amp;<br>Black Olives</p></div>
  <div class="pr"><div class="tag tag--sm tag--dark" style="top:152px">$11.99</div><div class="tag tag--sm tag--red" style="top:152px">$29.95</div></div>

  <div class="item item--r" style="top:207px"><h3>Mediterranean<br>Chicken</h3><p>Seasoned Chicken<br>Breast, Tomatoes, Red<br>Onions and Feta Cheese</p></div>
  <div class="pr"><div class="tag tag--sm tag--dark" style="top:209px">$11.99</div><div class="tag tag--sm tag--red" style="top:209px">$29.95</div></div>

  <div class="item item--r" style="top:269px"><h3>Original Spinach</h3><p>Spinach &amp; Feta Cheese</p></div>
  <div class="pr"><div class="tag tag--sm tag--dark" style="top:270px">$11.99</div><div class="tag tag--sm tag--red" style="top:270px">$29.95</div></div>

  <div class="item item--r" style="top:299px"><h3>Zeus</h3><p>Spinach, Feta Cheese<br>and Tomatoes</p></div>
  <div class="pr"><div class="tag tag--sm tag--dark" style="top:300px">$11.99</div><div class="tag tag--sm tag--red" style="top:300px">$29.95</div></div>

  <div class="item item--r" style="top:339px"><h3>Greek</h3><p>Feta Cheese, Tomato,<br>Green Peppers, Red<br>Onions and Black Olives</p></div>
  <div class="pr"><div class="tag tag--sm tag--dark" style="top:339px">$11.99</div><div class="tag tag--sm tag--red" style="top:339px">$29.95</div></div>

  <div class="item item--r" style="top:392px"><h3>Vegetarian</h3><p>Mushrooms, Tomatoes,<br>Green Peppers and Black<br>Olives</p></div>
  <div class="pr"><div class="tag tag--sm tag--dark" style="top:392px">$11.99</div><div class="tag tag--sm tag--red" style="top:392px">$29.95</div></div>

  <div class="item item--r" style="top:441px"><h3>Veggie Delight</h3><p>Mushrooms, Tomatoes,<br>Green Peppers, Black<br>Olives &amp; Onions</p></div>
  <div class="pr"><div class="tag tag--sm tag--dark" style="top:442px">$11.99</div><div class="tag tag--sm tag--red" style="top:442px">$29.95</div></div>

  <div class="item item--r" style="top:494px"><h3>Deluxe</h3><p style="margin-top:3px">Pepperoni, Mushrooms,<br>Ham, Tomatoes, Green<br>Peppers and Red Onions</p></div>
  <div class="pr"><div class="tag tag--sm tag--dark" style="top:494px">$11.99</div><div class="tag tag--sm tag--red" style="top:494px">$29.95</div></div>

  <div class="item item--r" style="top:548px"><h3>Calder Special</h3><p>Pepperoni, Mushrooms,<br>Ham, Green Peppers and<br>Black Olives</p></div>
  <div class="pr"><div class="tag tag--sm tag--dark" style="top:549px">$11.99</div><div class="tag tag--sm tag--red" style="top:549px">$29.95</div></div>

  <div class="abs pill">CALDER SPECIAL</div>
  <div class="item item--r" style="top:622px"><p>Crispy Dill Pickles, Fresh<br>Dill with our cream based<br>garlic sauce. Served with<br>our without bacon.</p></div>
  <div class="pr"><div class="tag tag--sm tag--dark" style="top:604px">$11.99</div><div class="tag tag--sm tag--red" style="top:604px">$29.95</div></div>

  <div class="abs back-logo">CALDER PIZZA</div>
  <svg class="abs" style="left:51px;top:731px" width="13" height="18" viewBox="0 0 13 18" aria-hidden="true">
    <path d="M6.5 0 C2.9 0 0 2.8 0 6.4 C0 11 6.5 18 6.5 18 S13 11 13 6.4 C13 2.8 10.1 0 6.5 0Z" fill="#c8251d"/>
    <circle cx="6.5" cy="6.3" r="2.5" fill="#f5f5f4"/>
  </svg>
  <p class="abs address">Fenwick Ridge Plaza<br>417, 318 9 Avenue SW</p>
  <p class="abs small-note" style="left:50px;top:770px;width:220px">For our complete appetizer, pasta, salad and catering menu visit our website</p>
  <p class="abs web" style="left:50px;top:801px">www.<strong>calderpizza</strong>.ca</p>

  <div class="abs pork">
    <h4>BBQ PULLED PORK</h4>
    <span class="mini mini--dark">$14.49</span>
    <span class="mini mini--light">$35.95</span>
    <p>Pulled Pork, Red Onions, Red Peppers and Cilantro</p>
  </div>

  <div class="photo photo--pizza-red" role="img" aria-label="Photo of a pepperoni and olive pizza with a slice pulled out" style="left:272px;top:738px;width:241px;height:241px"></div>
  <div class="photo photo--leaf" role="img" aria-label="Photo of a basil leaf" style="left:478px;top:752px;width:34px;height:24px"></div>
  <div class="photo photo--bowl" role="img" aria-label="Photo of a wooden bowl of fresh mozzarella balls" style="left:66px;top:847px;width:113px;height:113px"></div>
  <div class="photo photo--sauce" role="img" aria-label="Photo of a cup of tomato sauce" style="left:191px;top:856px;width:63px;height:63px"></div>
  <div class="photo photo--leaf" role="img" aria-label="Photo of a basil leaf" style="left:27px;top:853px;width:40px;height:56px"></div>
</section>

</body>
</html>
```